Business Card Design Project

Use our current logo. Clean design.

Industry/Entity Type

Business

Requirements
Must have
• Marisela DUBRANCQ
M. Law
Managing Partner

Alpenvorsa AG
Kornhalmweg 214
CH-3097 Liebefeld

M. +41 79 412 56 27
T. +41 31 928 44 10
F. +41 31 928 44 19

m.dubrancq@alpenvorsa-example.com
www.alpenvorsa-example.com

```html
<!DOCTYPE html>
<html lang="en">
<head>
<meta charset="utf-8">
<title>Alpenvorsa AG – Business Card</title>
<link rel="stylesheet" href="https://fonts.googleapis.com/css2?family=Jost:wght@400;500&family=Open+Sans:wght@700&display=swap">
<style>
  :root {
    --page-bg: #e7e4df;
    --card-light: #fbfbfb;
    --card-shade: #e4e4e4;
    --panel: #3e3e3e;
    --ink: #2e2e2e;
    --ink-soft: #3a3a3a;
    --on-panel: #ffffff;
  }
  * { margin: 0; padding: 0; box-sizing: border-box; }
  html, body {
    width: 1200px; height: 750px; overflow: hidden;
    background: var(--page-bg);
  }
  .business-card {
    position: absolute; left: 60px; top: 82px;
    width: 1080px; height: 587px;
    border-radius: 10px;
    background: radial-gradient(ellipse at 45% 30%, var(--card-light) 0%, #f1f1f1 55%, var(--card-shade) 100%);
    box-shadow: 0 4px 14px rgba(0,0,0,.18);
    overflow: hidden;
    font-family: "Jost", "Futura", sans-serif;
    color: var(--ink);
  }
  .brand-name {
    position: absolute; left: 40px; top: 240px; width: 440px;
    text-align: center;
    font-size: 56px; font-weight: 500; letter-spacing: 2px;
    color: var(--ink);
  }
  .web-bar {
    position: absolute; left: 0; top: 453px;
    width: 520px; height: 100px;
    background: var(--panel);
    border-radius: 0 12px 12px 0;
    display: flex; align-items: center; padding-left: 22px;
    font-family: "Open Sans", "Arial", sans-serif;
    font-weight: 700; font-size: 29px; color: var(--on-panel);
    letter-spacing: .3px;
  }
  .identity-panel {
    position: absolute; right: 0; top: 101px;
    width: 460px; height: 174px;
    background: var(--panel);
    border-radius: 12px 0 0 12px;
    padding: 10px 18px 0 0;
    text-align: right; color: var(--on-panel);
    font-size: 29px; line-height: 38px; font-weight: 400;
  }
  .identity-panel .email { font-size: 25px; line-height: 36px; }
  .contact-list { position: absolute; left: 760px; top: 300px; list-style: none; }
  .contact-row {
    position: absolute; left: 0; display: flex; align-items: flex-start;
    font-size: 30px; line-height: 47px; color: var(--ink-soft); white-space: nowrap;
  }
  .contact-row .icon { width: 44px; height: 44px; margin-right: 12px; flex: none; margin-top: 2px; }
  .contact-row .icon svg { width: 100%; height: 100%; fill: var(--ink-soft); }
  .row-address { top: 0; }
  .row-mobile { top: 103px; }
  .row-phone { top: 154px; }
  .row-fax { top: 203px; }
</style>
</head>
<body>
  <article class="business-card">
    <div class="brand-name">ALPENVORSA</div>

    <div class="web-bar">www.alpenvorsa-example.com</div>

    <div class="identity-panel">
      <div class="person">Marisela DUBRANCQ, M.Law</div>
      <div class="role">Managing Partner</div>
      <div class="company">Alpenvorsa AG</div>
      <div class="email">m.dubrancq@alpenvorsa-example.com</div>
    </div>

    <ul class="contact-list">
      <li class="contact-row row-address">
        <span class="icon"><svg viewBox="0 0 24 24" aria-hidden="true"><path d="M12 2a7 7 0 0 0-7 7c0 5 7 13 7 13s7-8 7-13a7 7 0 0 0-7-7zm0 9.5A2.5 2.5 0 1 1 12 6.5a2.5 2.5 0 0 1 0 5z"/></svg></span>
        <span>Kornhalmweg 214<br>CH-3097 Liebefeld</span>
      </li>
      <li class="contact-row row-mobile">
        <span class="icon"><svg viewBox="0 0 24 24" aria-hidden="true"><path d="M8 1h1v3h6a1 1 0 0 1 1 1v17a1 1 0 0 1-1 1H9a1 1 0 0 1-1-1zm2 5v5h4V6zm0 7v2h1v-2zm2 0v2h1v-2zm-2 3v2h1v-2zm2 0v2h1v-2zm-2 3v2h1v-2zm2 0v2h1v-2z"/></svg></span>
        <span>+41 79 412 56 27</span>
      </li>
      <li class="contact-row row-phone">
        <span class="icon"><svg viewBox="0 0 24 24" aria-hidden="true"><path d="M3 8c0-2 4-4 9-4s9 2 9 4v2h-4V8.5c-1-.6-3-1-5-1s-4 .4-5 1V10H3zm4 3h10l3 5v5H4v-5zm2 2v1h2v-1zm3 0v1h2v-1zm3 0v1h-1 2zm-6 3v1h2v-1zm3 0v1h2v-1zm3 0v1h2v-1z"/></svg></span>
        <span>+41 31 928 44 10</span>
      </li>
      <li class="contact-row row-fax">
        <span class="icon"><svg viewBox="0 0 24 24" aria-hidden="true"><path d="M6 2h9l3 3v5H6zm-3 9h18a1 1 0 0 1 1 1v7a1 1 0 0 1-1 1h-3v-4H6v4H3a1 1 0 0 1-1-1v-7a1 1 0 0 1 1-1zm4 6h10v6H7z"/></svg></span>
        <span>+41 31 928 44 19</span>
      </li>
    </ul>
  </article>
</body>
</html>
```